van Kalder Jewelry & Co. needs a website design

We need a website design for a new company based in Minnesota called 'van Kalder Jewelry & Co.' My wife and I are both geologists who handcraft fine jewelry using nephrite-jade from a newly discovered glacial deposit in Minnesota that I independently discovered, researched, and extracted. The jade colors range from a beautiful black to dark green and are mostly set in yellow gold, though we also use silver, platinum, and white gold. We will also be using nephrite-jade, jadeite-jade's from other parts of the world, including other semi- precious and precious stones such as black onyx/ chalcedony's, rubies ,sapphire, and diamonds. The family name 'van Kalder' means of the ash tree in French, and I would this motif to be incorporated into the website design. I've attached the files for our company logo and would like to blend that theme and emblem into the design as well in an elegant fashion. I'm aiming for a black jade/ dark green and yellow gold look am primarily interested in a design optimized for online shoppers. Additionally, I want a section where visitors can read a brief summary of our research and discovery story as geologists. Currently, we will be selling pendant necklaces, bead necklaces, earrings, bead bracelets, and bracelets. The website should convey that we sell fine, handcrafted, and very unique jewelry.

```html
<!DOCTYPE html>
<html lang="en">
<head>
<meta charset="utf-8">
<title>van Kalder Jewelry &amp; Co.</title>
<link href="https://fonts.googleapis.com/css2?family=Noto+Serif:wght@400;500;600&display=swap" rel="stylesheet">
<style>
:root{
  --hero-bg:#1a1218;
  --page-bg:#1c1b1d;
  --jade:#1e453d;
  --gold:#c99a04;
  --gold-light:#e2bd3a;
  --white:#ffffff;
  --muted:#d8d4d0;
  --ink:#1a1a1a;
}
*{margin:0;padding:0;box-sizing:border-box}
html,body{width:1200px;height:3229px;overflow:hidden;background:var(--page-bg)}
body{font-family:"Noto Serif",Georgia,serif;color:var(--white)}
h1,h2{font-weight:400}
a{text-decoration:none}
.page{position:relative;width:1200px;height:3229px;overflow:hidden;background:var(--page-bg)}
.abs{position:absolute}

/* hero */
.hero{left:0;top:0;width:1200px;height:562px;background:var(--hero-bg)}
.hero-photo{left:498px;top:0;width:702px;height:562px;background:radial-gradient(ellipse at 55% 40%,#c9a38c 0%,#7a4a36 38%,#3a2228 70%,var(--hero-bg) 100%)}
.brand{left:105px;top:16px;width:106px;text-align:center}
.brand-mark{display:block;margin:0 auto 8px;width:26px;height:26px;border:1.5px solid var(--gold)}
.brand-name{font-size:15px;letter-spacing:1px;color:var(--gold-light);white-space:nowrap}
.brand-sub{font-size:6px;letter-spacing:2px;color:var(--gold);margin-top:2px;white-space:nowrap}
.nav{top:58px;left:521px;display:flex;gap:38px;font-size:14px;font-weight:500;text-transform:uppercase}
.nav a{color:var(--white)}
.nav-tools{left:1035px;top:58px;display:flex;gap:16px}
.hero-title{left:105px;top:170px;font-size:40px;font-weight:500;line-height:49px}
.hero-text{left:105px;top:285px;width:400px;font-size:15.5px;line-height:20px;color:var(--muted)}
.btn{display:block;background:var(--gold);color:var(--white);font-size:11px;text-align:center;text-transform:uppercase;letter-spacing:.4px}
.hero-btn{left:105px;top:360px;width:124px;height:30px;line-height:30px}
.ornament-v{left:491px;top:545px;width:235px;height:144px;background:linear-gradient(135deg,#e9c84a 0%,#c99a04 55%,#6b4f00 100%);clip-path:polygon(0 2%,100% 2%,50% 100%)}

/* collection */
.eyebrow{left:0;top:760px;width:1200px;text-align:center;font-size:15px;text-transform:uppercase;font-weight:500}
.section-title{left:0;top:793px;width:1200px;text-align:center;font-size:38px;line-height:48px}
.categories{left:105px;top:939px;display:flex;gap:17.5px}
.category{position:relative;width:184px;height:195px;background:var(--gold)}
.category::after{content:"";position:absolute;inset:11px;border:1.5px solid rgba(255,255,255,.85)}
.category svg{position:absolute;left:50%;top:34px;transform:translateX(-50%)}
.category span{position:absolute;left:0;right:0;top:128px;text-align:center;font-size:14px}

/* history */
.jade-band{left:0;top:1375px;width:1200px;height:694px;background:var(--jade)}
.photo-earring{left:105px;top:1308px;width:402px;height:496px;background:linear-gradient(135deg,#f4f1ef 0%,#d9b8a8 45%,#c9372f 100%)}
.history-title{left:601px;top:1446px;font-size:38px;color:var(--gold);font-weight:500}
.history-text{left:603px;top:1522px;width:490px;font-size:15.5px;line-height:20.2px;color:var(--muted)}
.photo-ring{left:612px;top:1744px;width:435px;height:429px;background:linear-gradient(160deg,#e9ece8 0%,#d8b7a2 45%,#2a2a2c 75%,#1a1a1c 100%)}

/* products */
.popular-title{left:102px;top:2240px;font-size:38px;font-weight:500}
.slider-arrows{left:970px;top:2278px;display:flex;gap:22px}
.products{left:105px;top:2349px;display:flex;gap:17px}
.product{position:relative;width:235px;height:277px;background:var(--white);color:var(--ink);text-align:center}
.product-photo{position:absolute;left:14px;top:12px;width:207px;height:140px}
.product-name{position:absolute;left:0;right:0;top:170px;font-size:15px;font-weight:500}
.product-price{position:absolute;left:0;right:0;top:194px;font-size:15px;color:var(--gold)}
.product .btn{position:absolute;left:55px;top:226px;width:124px;height:29px;line-height:29px;text-transform:none;font-size:11px}

/* testimonial */
.testimonial-photo{left:202px;top:2711px;width:572px;height:359px;background:radial-gradient(ellipse at 60% 55%,#5a5a5c 0%,#2c2c2e 50%,var(--page-bg) 100%)}
.stars{left:0;top:2800px;width:1200px;display:flex;justify-content:center;gap:6px}
.quote{left:285px;top:2868px;width:630px;text-align:center;font-size:16px;line-height:20px;color:var(--muted)}

/* footer */
.footer{left:0;top:3070px;width:1200px;height:159px;background:var(--gold)}
.footer-brand{left:120px;top:3094px;width:132px;text-align:center}
.footer-brand .brand-mark{border-color:rgba(255,255,255,.8)}
.footer-brand .brand-name{color:rgba(255,255,255,.85);font-size:17px}
.footer-nav{left:374px;top:3126px;display:flex;gap:38px;font-size:15px;font-weight:500;text-transform:uppercase}
.footer-nav a{color:var(--white)}
.social{left:896px;top:3126px;display:flex;gap:18px}
.social span{display:block;width:22px;height:22px;border-radius:50%;background:var(--white)}
</style>
</head>
<body>
<div class="page">

  <section class="abs hero"></section>
  <div class="abs hero-photo" role="img" aria-label="Portrait of a model wearing a diamond necklace and earrings"></div>

  <div class="abs brand">
    <span class="brand-mark"></span>
    <div class="brand-name">VAN KALDER</div>
    <div class="brand-sub">JEWELRY &amp; CO.</div>
  </div>

  <nav class="abs nav">
    <a href="#">Home</a><a href="#">About Us</a><a href="#">Products</a><a href="#">Contact Us</a>
  </nav>
  <div class="abs nav-tools">
    <svg width="16" height="16" viewBox="0 0 16 16" fill="none" stroke="#fff" stroke-width="1.8"><circle cx="7" cy="7" r="5"/><path d="M11 11l4 4"/></svg>
    <svg width="15" height="16" viewBox="0 0 15 16" fill="none" stroke="#fff" stroke-width="1.8"><rect x="1.5" y="5" width="12" height="10" rx="2"/><path d="M4.5 5V4a3 3 0 016 0v1"/></svg>
  </div>

  <h1 class="abs hero-title">Diamond Jewellery<br>Collection</h1>
  <p class="abs hero-text">Lorem ipsum dolor sit amet consectetur. Diam nunc fermentum vitae id.</p>
  <a class="abs btn hero-btn" href="#">Shop Now</a>

  <div class="abs ornament-v" role="img" aria-label="Gold decorative ornament"></div>

  <p class="abs eyebrow">Our Collection</p>
  <h2 class="abs section-title">Wearing jewelry is a way to<br>express yourself without a word</h2>

  <div class="abs categories">
    <div class="category">
      <svg width="80" height="80" viewBox="0 0 80 80" fill="none" stroke="#fff" stroke-width="2"><path d="M8 4 Q40 60 72 4"/><path d="M34 56 L46 56 L50 64 L40 76 L30 64 Z"/></svg>
      <span>Pendant Necklaces</span>
    </div>
    <div class="category">
      <svg width="80" height="80" viewBox="0 0 80 80" fill="none" stroke="#fff" stroke-width="2"><circle cx="40" cy="42" r="28"/><circle cx="40" cy="12" r="4"/></svg>
      <span>Bead Necklaces</span>
    </div>
    <div class="category">
      <svg width="80" height="80" viewBox="0 0 80 80" fill="none" stroke="#fff" stroke-width="2"><circle cx="26" cy="10" r="4"/><circle cx="54" cy="10" r="4"/><path d="M26 14v24M54 14v24"/><circle cx="26" cy="54" r="10"/><circle cx="54" cy="54" r="10"/></svg>
      <span>Earrings</span>
    </div>
    <div class="category">
      <svg width="80" height="80" viewBox="0 0 80 80" fill="none" stroke="#fff" stroke-width="2"><circle cx="40" cy="40" r="30"/><circle cx="40" cy="40" r="24"/></svg>
      <span>Bead Bracelets</span>
    </div>
    <div class="category">
      <svg width="80" height="80" viewBox="0 0 80 80" fill="none" stroke="#fff" stroke-width="2"><ellipse cx="40" cy="40" rx="36" ry="24"/><ellipse cx="40" cy="40" rx="30" ry="18"/><circle cx="32" cy="62" r="4"/><circle cx="48" cy="62" r="4"/></svg>
      <span>Bracelets</span>
    </div>
  </div>

  <section class="abs jade-band"></section>
  <div class="abs photo-earring" role="img" aria-label="Close-up of a woman wearing a silver hoop earring"></div>
  <h2 class="abs history-title">Our History</h2>
  <p class="abs history-text">Lorem ipsum dolor sit amet consectetur. Diam nunc fermentum vitae id. Sed ipsum habitant velit varius in volutpat. Sollicitudin sed risus blandit blandit. Consectetur scelerisque ut adipiscing cursus. Vitae ullamcorper dui nascetur amet dictum habitant habitasse scelerisque. Sem pretium id dolor mauris quis habitant dictum vulputate. Proin convallis posuere adipiscing cras dolor est hendrerit ut. At quis amet quam nisi posuere feugiat eu mauris. Non egestas ullamcorper sit diam amet eget magna neque. Ornare sed nibh diam leo at.</p>
  <div class="abs photo-ring" role="img" aria-label="Hand wearing gold rings resting on a black leather bag"></div>

  <h2 class="abs popular-title">Popular Jewelry</h2>
  <div class="abs slider-arrows">
    <svg width="30" height="24" viewBox="0 0 30 24" fill="none" stroke="#c99a04" stroke-width="2.5"><path d="M28 12H3M12 3L3 12l9 9"/></svg>
    <svg width="30" height="24" viewBox="0 0 30 24" fill="none" stroke="#c99a04" stroke-width="2.5"><path d="M2 12h25M18 3l9 9-9 9"/></svg>
  </div>

  <div class="abs products">
    <div class="product">
      <div class="product-photo" role="img" aria-label="Silver ring with a blue gemstone" style="background:radial-gradient(circle at 50% 50%,#5ec3e8 0%,#c9d3d8 35%,#fff 70%)"></div>
      <div class="product-name">Blue Diamond</div><div class="product-price">$100</div>
      <a class="btn" href="#">Add to cart</a>
    </div>
    <div class="product">
      <div class="product-photo" role="img" aria-label="Heart-shaped violet gemstone pendant" style="background:radial-gradient(circle at 52% 60%,#6a5ab8 0%,#b7b0d6 30%,#fff 65%)"></div>
      <div class="product-name">Blue Diamond</div><div class="product-price">$100</div>
      <a class="btn" href="#">Add to cart</a>
    </div>
    <div class="product">
      <div class="product-photo" role="img" aria-label="Set of orange gemstone jewellery pieces" style="background:radial-gradient(ellipse at 50% 50%,#d0571c 0%,#e7a882 35%,#fff 70%)"></div>
      <div class="product-name">Blue Diamond</div><div class="product-price">$100</div>
      <a class="btn" href="#">Add to cart</a>
    </div>
    <div class="product">
      <div class="product-photo" role="img" aria-label="Ring with a large pale green gemstone" style="background:radial-gradient(circle at 50% 45%,#b7e3b0 0%,#7d8a80 40%,#fff 72%)"></div>
      <div class="product-name">Blue Diamond</div><div class="product-price">$100</div>
      <a class="btn" href="#">Add to cart</a>
    </div>
  </div>

  <div class="abs testimonial-photo" role="img" aria-label="Monochrome close-up of an ornate filigree hoop earring"></div>
  <div class="abs stars">
    <svg width="28" height="27" viewBox="0 0 24 23"><path d="M12 0l3.5 7.5 8.5 1-6.3 5.8 1.7 8.4L12 18.5 4.6 22.7l1.7-8.4L0 8.5l8.5-1z" fill="#f5b800"/></svg>
    <svg width="28" height="27" viewBox="0 0 24 23"><path d="M12 0l3.5 7.5 8.5 1-6.3 5.8 1.7 8.4L12 18.5 4.6 22.7l1.7-8.4L0 8.5l8.5-1z" fill="#f5b800"/></svg>
    <svg width="28" height="27" viewBox="0 0 24 23"><path d="M12 0l3.5 7.5 8.5 1-6.3 5.8 1.7 8.4L12 18.5 4.6 22.7l1.7-8.4L0 8.5l8.5-1z" fill="#f5b800"/></svg>
    <svg width="28" height="27" viewBox="0 0 24 23"><path d="M12 0l3.5 7.5 8.5 1-6.3 5.8 1.7 8.4L12 18.5 4.6 22.7l1.7-8.4L0 8.5l8.5-1z" fill="#f5b800"/></svg>
    <svg width="28" height="27" viewBox="0 0 24 23"><path d="M12 0l3.5 7.5 8.5 1-6.3 5.8 1.7 8.4L12 18.5 4.6 22.7l1.7-8.4L0 8.5l8.5-1z" fill="#f5b800"/></svg>
  </div>
  <p class="abs quote">“It's good to start early when buying jewelry pieces. Aside from being investments, they are classic, they are timeless, and they are something that you pass on - it's a memory, it's an heirloom.”</p>

  <footer class="abs footer"></footer>
  <div class="abs footer-brand">
    <span class="brand-mark"></span>
    <div class="brand-name">VAN KALDER</div>
  </div>
  <nav class="abs footer-nav">
    <a href="#">Home</a><a href="#">About Us</a><a href="#">Products</a><a href="#">Contact Us</a>
  </nav>
  <div class="abs social" aria-label="Social media links">
    <span></span><span></span><span></span><span></span>
  </div>

</div>
</body>
</html>
```